FSA Expiring Soon 2023

Hi,
Looking to upgrade the design of current flyer to be used as an e-blast.
-8.5"x11"
-Under 5MB
-Several formats, PDF, .ai, jpeg, png

This flyer should be simple, yet eye catching. The goal is to remind patients that their Flexible Spending Account (FSA) will be expiring soon and that they can use their FSA or HSA to purchase most of our over the counter items, including inserts and shoes.

-must include: Some insurance plans require a letter of medical necessity
-must include: Each flexible spending account varies on their expiration date
- stock images must be free

I'll attach our logo and old flyer as well for reference.

Thank you,
Brody

```html
<!DOCTYPE html>
<html lang="en">
<head>
<meta charset="utf-8">
<title>FSA Expiring Soon – Fairview Foot &amp; Ankle</title>
<link rel="stylesheet" href="https://fonts.googleapis.com/css2?family=Red+Hat+Display:ital,wght@0,500;0,700;0,800;0,900;1,700;1,800&display=swap">
<style>
  :root {
    --orange: #f47a3c;
    --orange-light: #f08e2e;
    --teal: #4fc1a3;
    --blue: #4eb0e3;
    --ink: #1b1b1b;
    --black: #000000;
    --white: #ffffff;
    --backdrop: #e9e6e0;
  }
  * { margin: 0; padding: 0; box-sizing: border-box; }
  html, body { width: 1200px; height: 1117px; overflow: hidden; }
  body {
    background: var(--backdrop);
    font-family: "Red Hat Display", sans-serif;
    position: relative;
  }
  .flyer {
    position: absolute;
    left: 177px; top: 20px;
    width: 846px; height: 1077px;
    background: var(--white);
    overflow: hidden;
  }
  .side-bar {
    position: absolute; right: 0; top: 0;
    width: 22px; height: 502px;
    background: linear-gradient(180deg, var(--blue), var(--teal));
  }
  .brand-dot {
    position: absolute; left: 72px; top: 40px;
    width: 130px; height: 130px; border-radius: 50%;
    background: var(--teal);
  }
  .brand-name {
    position: absolute; right: 72px; top: 44px;
    text-align: right;
    font-family: "Red Hat Display", sans-serif;
    font-weight: 900;
    color: var(--orange);
    font-size: 60px; line-height: 64px;
    letter-spacing: -1px;
  }
  .brand-web {
    position: absolute; right: 72px; top: 176px;
    font-family: "Red Hat Display", sans-serif;
    font-weight: 900; color: var(--orange);
    font-size: 24px; letter-spacing: -0.3px;
  }
  .dot-grid {
    position: absolute; left: 85px; top: 262px;
    display: grid; grid-template-columns: repeat(6, 4px);
    column-gap: 14px; row-gap: 13px;
  }
  .dot-grid span { width: 4px; height: 4px; border-radius: 50%; background: var(--blue); }
  .photo-frame {
    position: absolute; left: 387px; top: 280px;
    width: 408px; height: 393px;
    background: var(--white);
    border-radius: 0 48px 0 0;
    z-index: 1;
  }
  .photo {
    position: absolute; left: 397px; top: 290px;
    width: 388px; height: 372px;
    border-radius: 0 42px 0 28px;
    background: linear-gradient(135deg, #6b4a2c 0%, #e4a534 28%, #efe4c4 48%, #b9b7b0 68%, #4f5a60 100%);
    z-index: 1;
  }
  .badge {
    position: absolute; left: 215px; top: 250px;
    width: 419px; height: 67px;
    background: linear-gradient(90deg, var(--blue), var(--teal));
    border-radius: 14px;
    transform: skewX(-6deg);
    display: flex; align-items: center; justify-content: center;
    box-shadow: 0 0 0 6px var(--white);
    z-index: 3;
  }
  .badge span {
    transform: skewX(6deg);
    color: var(--white);
    font-weight: 900; font-size: 42px; letter-spacing: -0.5px;
    white-space: nowrap;
    text-shadow: 1px 2px 2px rgba(0,0,0,0.35);
  }
  .headline {
    position: absolute; left: 77px; top: 344px;
    width: 310px;
    font-weight: 900; color: var(--ink);
    font-size: 25px; line-height: 30px;
    white-space: nowrap;
  }
  .orange-band {
    position: absolute; left: 0; top: 593px;
    width: 846px; height: 150px;
    background: linear-gradient(90deg, var(--orange) 0%, var(--orange-light) 50%, var(--orange) 100%);
  }
  .eligible-box {
    position: absolute; left: 82px; top: 515px;
    width: 305px; height: 158px;
    background: var(--white);
    border-top: 4px solid var(--orange);
    border-left: 4px solid var(--orange);
    border-radius: 22px 0 0 12px;
    padding: 16px 10px 0 34px;
    font-weight: 500; color: var(--ink);
    font-size: 22px; line-height: 24.5px;
    z-index: 2;
  }
  .insurance-note {
    position: absolute; left: 0; top: 693px; width: 846px;
    text-align: center; color: var(--white);
    font-weight: 700; font-size: 23.5px;
  }
  .expiry-note {
    position: absolute; left: 0; top: 757px; width: 846px;
    text-align: center; color: var(--ink);
    font-weight: 800; font-style: italic; font-size: 17px;
  }
  .offices {
    position: absolute; left: 0; top: 794px;
    width: 846px; height: 283px;
    background: var(--black);
  }
  .office { position: absolute; top: 33px; color: var(--white); }
  .office h3 {
    height: 34px; background: var(--teal);
    border-radius: 3px;
    font-weight: 700; font-size: 19px;
    display: flex; align-items: center; justify-content: center;
  }
  .office p {
    margin-top: 10px;
    font-weight: 500; font-size: 18.5px; line-height: 24px;
  }
  .office-north { left: 82px; }
  .office-north h3 { width: 190px; }
  .office-mill { left: 314px; }
  .office-mill h3 { width: 190px; }
  .office-cedar { left: 545px; }
  .office-cedar h3 { width: 219px; }
  .divider {
    position: absolute; top: 33px; width: 2px; height: 112px;
    background: var(--blue);
  }
  .contact-tab {
    position: absolute; left: 0; top: 955px;
    width: 846px; height: 122px;
  }
  .contact-row {
    position: absolute; left: 0; top: 1008px; width: 846px;
    display: flex; justify-content: center; align-items: center;
    gap: 20px;
    font-weight: 800; font-size: 28px; color: var(--ink);
  }
  .contact-item { display: flex; align-items: center; gap: 12px; }
  .contact-item svg { width: 30px; height: 30px; }
  .contact-sep { width: 3px; height: 44px; background: var(--teal); }
</style>
</head>
<body>
  <main class="flyer">
    <div class="side-bar"></div>

    <div class="brand-dot"></div>
    <div class="brand-name">FAIRVIEW<br>FOOT &amp; ANKLE</div>
    <div class="brand-web">STRIDEWELLFEET.COM</div>

    <div class="dot-grid">
      <span></span><span></span><span></span><span></span><span></span><span></span>
      <span></span><span></span><span></span><span></span><span></span><span></span>
      <span></span><span></span><span></span><span></span><span></span><span></span>
    </div>

    <div class="orange-band"></div>

    <div class="photo-frame"></div>
    <div class="photo" role="img" aria-label="Photo of an orange pill bottle spilling white tablets beside a stethoscope on dollar bills"></div>

    <div class="badge"><span>EXPIRING SOON!</span></div>

    <h1 class="headline">USE YOUR FLEXIBLE<br>SPENDING ACCOUNT<br>FUNDS BEFORE<br>THEY EXPIRE AT THE<br>END OF THE YEAR!</h1>

    <p class="eligible-box">most of our over the counter products are FSA/HSA eligible, including inserts and shoes.</p>

    <p class="insurance-note">Some insurance plans require a letter of medical necessity</p>
    <p class="expiry-note">Each flexible spending account varies on their expiration date</p>

    <section class="offices">
      <div class="office office-north">
        <h3>Northgate Office</h3>
        <p>218 Linden Park<br>Dr. Ste. 110<br>Northgate, MD 21790</p>
      </div>
      <div class="divider" style="left:294px"></div>
      <div class="office office-mill">
        <h3>Millbrook Office</h3>
        <p>4520 Harwell<br>Blvd. Ste. 305<br>Millbrook, MD 21795</p>
      </div>
      <div class="divider" style="left:524px"></div>
      <div class="office office-cedar">
        <h3>Cedar Ridge Office</h3>
        <p>77 Wellness Way<br>Cedar Ridge, WV&nbsp; 25499</p>
      </div>
    </section>

    <svg class="contact-tab" viewBox="0 0 846 122" aria-hidden="true">
      <defs>
        <linearGradient id="tabEdge" x1="0" x2="1" y1="0" y2="0">
          <stop offset="0" stop-color="#4eb0e3"/>
          <stop offset="1" stop-color="#4fc1a3"/>
        </linearGradient>
      </defs>
      <path d="M59 126 L98 42 Q111 14 142 14 L704 14 Q735 14 748 42 L788 126 Z" fill="#ffffff" stroke="url(#tabEdge)" stroke-width="10"/>
    </svg>

    <div class="contact-row">
      <span class="contact-item">
        <svg viewBox="0 0 30 30" aria-hidden="true">
          <circle cx="15" cy="15" r="15" fill="#f47a3c"/>
          <g fill="none" stroke="#fff" stroke-width="1.6">
            <circle cx="15" cy="15" r="8"/>
            <ellipse cx="15" cy="15" rx="3.5" ry="8"/>
            <line x1="7" y1="15" x2="23" y2="15"/>
            <line x1="8.5" y1="11" x2="21.5" y2="11"/>
            <line x1="8.5" y1="19" x2="21.5" y2="19"/>
          </g>
        </svg>
        StrideWellFeet.com
      </span>
      <span class="contact-sep"></span>
      <span class="contact-item">
        <svg viewBox="0 0 30 30" aria-hidden="true">
          <circle cx="15" cy="15" r="15" fill="#f47a3c"/>
          <path d="M10.5 8.5 L13 8 L14.5 11.8 L12.8 13.2 Q14.3 16.2 17 17.4 L18.5 15.6 L22 17 L21.6 19.6 Q20.8 21.5 18.5 21.3 Q10.5 20 8.7 11.5 Q8.6 9.3 10.5 8.5 Z" fill="#fff"/>
        </svg>
        (555)014-2270
      </span>
    </div>
  </main>
</body>
</html>
```